【 概要 】 ECサイトで販売中の小さなお子様向けベビースタイ(よだれかけ)の メインバナー、サブ画像×2 を制作していただけるデザイナー様を募集致します。 【 依頼内容 】 ・サイズ: 横2000× 縦3000px ・作成数: 3種類(メインバナー、サブ画像2枚)を 上記にリサイズして3種 ・利用用途:SNS広告、VORDAXサイトなどの商品画像 【ご応募条件】 ・イラストレーター、フォトショップを使用できる方 ・納品時にai形式またはpsd形式で納品できる方 【 デザインイメージ 】 ・ターゲット層:小さなお子様を持つ親御様 ・雰囲気:安心感、清潔感、暖かみ ※募集要項の”希望する色”はお気になさらず 自由な色でご製作お願いします ・参考デザイン: ①Lumatta https://shop.lumatta-example.jp/pages/trialpage?src=7&ref=Qx84TbWm2PzLk9VdRf3NcYh6GsJu0EaXw1KtBnZq5MoHy7Ci https://www.lumatta-example.jp/ ②tarvi https://jp.tarvi-example.com/ja/home.html ③felsu https://www.felsu-example.jp/?ref=Kq72LmWnBx4TzPd9Hs6VcYr1JgEuXa8NoQw3FtRi5ZbMyK0Ch 【依頼内容】 メインバナー 目を惹き購買意欲のある方が思わずクリックしたくなるような デザイン、キャッチフレーズ ○360℃使える防水スタイ(よだれかけ) ○6枚セット ○フリルスタイ 上記をアピールできるバナー 必須文言 6枚セット 360℃使える フリルスタイ 添付画像 画像の数は自由です(必ず1つは使用すること) キャッチフレーズ サブ画像×2 ○通気性 吸水性 速乾性 ○表地綿100% ○ホルムアルデヒド試験合格 ○国の基準値ホルムアルデヒド試験合格した商品であること(国の基準0.05以下) ○日本の第三者機関で安全性を確認した商品であること ○安心安全国内検品 サブ画像はメインバナーの詳細説明、安心して使用していただけることを アピールできるような制作をお願い致します。 ”必須文言なし” 添付画像は⑧必ず使用してください(国の基準値ホルムアルデヒド試験合格した商品であることの証明書のため) ○画像サイズ大小は問いません。 ○添付画像⑧に記載されている文字は見えなくも良い ご注意 画像や人物など追加してもok 他でデザインや商標の転用など、他社の 知的財産権を浸すことはNG 他のクライアント様へ提案した画像はNG 今後、画像は再利用する可能性がございます 【 契約金額(税抜) 】 1万円 ※契約金額(税込)からシステム利用料を差し引いた金額が、ワーカー様の受け取り金額となります その他ご質問等ありましたら、気軽にお問い合わせください。 ご応募をお待ちしております! |
どの案も素敵でしたが
お子様モデルがいない中
モデルのお子様のお写真と商品のよだれかけを組み合わせ
お客様によりイメージが湧きやすく安心、安全という観点からも一目でわかるような画像を作成していた
だき
こちらの作品が弊社のイメージに近く採用させていただきました。
この度はバナーコンペにご応募いただきありがとうございました。
この度は当社のバナーコンペに
ご応募いただきありがとうございました。
素晴らしいバナー提案をありがとうございます。
厳正なる選考の結果、誠に残念ではございますが、 今回はご希望に添いかねる結果となりましたことをお伝えいたします。 大変恐縮ではございますが、ご了承くださいますようお願い申し上げます。
また機会がありましたら是非お願いしたいと思っております。

```html
<!DOCTYPE html>
<html lang="ja">
<head>
<meta charset="utf-8">
<title>フリルスタイ 6枚セット メインバナー</title>
<link href="https://fonts.googleapis.com/css2?family=Zen+Maru+Gothic:wght@500;700;900&display=swap" rel="stylesheet">
<style>
  :root {
    --bg: #f7f1e7;
    --gold: #e9c35c;
    --tan: #b3946c;
    --tan-light: #e9dcc6;
    --blue-deep: #6f879d;
    --drop: #a9c1d8;
    --ink: #7a6a58;
    --white: #ffffff;
  }
  * { margin: 0; padding: 0; box-sizing: border-box; }
  html, body { width: 800px; height: 1200px; overflow: hidden; }
  body {
    background: var(--bg);
    font-family: "Zen Maru Gothic", sans-serif;
    color: var(--ink);
  }
  .banner {
    position: relative;
    width: 800px;
    height: 1200px;
    overflow: hidden;
    background: radial-gradient(circle at 50% 45%, #fbf7ef 0%, var(--bg) 70%);
  }
  .hero-photo {
    position: absolute;
    left: 40px;
    top: -20px;
    width: 420px;
    height: 410px;
    border-radius: 50%;
    background: radial-gradient(circle at 50% 55%, #f3ead9 0%, #e3d2b4 45%, #c9ad82 100%);
  }
  .waterproof {
    position: absolute;
    left: 470px;
    top: 130px;
    width: 280px;
    text-align: center;
  }
  .waterproof-lead {
    font-size: 32px;
    font-weight: 700;
    line-height: 1.2;
    letter-spacing: 2px;
  }
  .waterproof-word {
    display: inline-block;
    margin: 12px 0 8px;
    padding: 2px 26px;
    font-size: 72px;
    line-height: 1.1;
    font-weight: 900;
    color: var(--blue-deep);
    background: var(--white);
    border-radius: 18px;
    letter-spacing: 4px;
    box-shadow: 0 4px 0 var(--tan-light);
  }
  .waterproof-tail {
    font-size: 28px;
    font-weight: 700;
    line-height: 1.2;
    text-align: right;
  }
  .drops { position: absolute; left: 720px; top: 40px; }
  .headline-rule {
    position: absolute;
    left: 60px;
    width: 680px;
    height: 3px;
    background: var(--tan-light);
  }
  .headline-rule.top { top: 428px; }
  .headline-rule.bottom { top: 582px; }
  .headline-main {
    position: absolute;
    top: 450px;
    left: 0;
    width: 800px;
    text-align: center;
    font-size: 100px;
    line-height: 1.1;
    font-weight: 900;
    color: var(--gold);
    white-space: nowrap;
    text-shadow: 4px 4px 0 var(--white), 6px 6px 0 var(--tan-light);
  }
  .headline-main .small { font-size: 78px; }
  .headline-sub {
    position: absolute;
    top: 604px;
    left: 150px;
    width: 500px;
    height: 78px;
    line-height: 78px;
    text-align: center;
    font-size: 58px;
    font-weight: 700;
    color: var(--tan);
    background: var(--white);
    border-radius: 40px;
    letter-spacing: 8px;
  }
  .all-direction {
    position: absolute;
    left: 50px;
    top: 700px;
    font-size: 26px;
    line-height: 1.2;
    font-weight: 700;
    letter-spacing: 2px;
  }
  .cotton-accent {
    position: absolute;
    left: 80px;
    top: 830px;
    width: 100px;
    height: 100px;
    border-radius: 50%;
    background: radial-gradient(circle, #ffffff 0%, #efe6d6 70%, transparent 72%);
  }
  .product-photo {
    position: absolute;
    left: 180px;
    top: 750px;
    width: 640px;
    height: 470px;
    border-radius: 60px 0 0 0;
    background: linear-gradient(160deg, #efe9c8 0%, #e7efd9 35%, #f2dcc3 70%, #f0cfa8 100%);
  }
  .set-badge {
    position: absolute;
    left: 90px;
    top: 960px;
    width: 150px;
    height: 150px;
    border-radius: 50%;
    background: var(--white);
    border: 3px solid var(--tan);
    display: flex;
    flex-direction: column;
    align-items: center;
    justify-content: center;
    color: var(--tan);
    font-weight: 900;
    line-height: 1.1;
  }
  .set-badge .count { font-size: 40px; }
  .set-badge .unit { font-size: 30px; }
</style>
</head>
<body>
  <main class="banner">
    <div class="hero-photo" role="img" aria-label="編みかごの上に置かれたフリルスタイと綿花の写真"></div>

    <section class="waterproof">
      <p class="waterproof-lead">＼うれしい／</p>
      <p class="waterproof-word">防水</p>
      <p class="waterproof-tail">機能付き!</p>
    </section>

    <svg class="drops" width="60" height="60" viewBox="0 0 70 70" aria-hidden="true">
      <path d="M20 8 C26 20 32 27 32 34 a12 12 0 0 1 -24 0 C8 27 14 20 20 8Z" fill="var(--drop)"/>
      <path d="M50 30 C54 38 58 42 58 47 a8 8 0 0 1 -16 0 C42 42 46 38 50 30Z" fill="var(--drop)"/>
    </svg>

    <div class="headline-rule top"></div>
    <h1 class="headline-main">360°<span class="small">の</span>安心感</h1>
    <div class="headline-rule bottom"></div>
    <p class="headline-sub">フリルスタイ</p>

    <p class="all-direction">全方位使えます</p>

    <div class="product-photo" role="img" aria-label="色違いのフリルスタイ6枚を並べた商品写真"></div>
    <div class="cotton-accent" role="img" aria-label="綿花の写真"></div>

    <div class="set-badge">
      <span class="count">6枚</span>
      <span class="unit">セット</span>
    </div>
  </main>
</body>
</html>
```